QuorintaFields background design

The task is to create a modern looking and very attractive background for the quorintaFields laboratory results reports + cover-page for the reports that matches the same design.

The background should be beautiful but also minimalistic enough not to interfere with the content inside the reports. If the background behind the content is too intensive then it is difficult to read the content. Our LOGO is blue and we have used blue-ish colors so far so perhaps one should try to keep blue at least as one of the colors. We have preferred to keep the design abstract/minimalistic rather than using photos.

Please look at the attached files, especially the file "Report with the current background" where you will see how the content is layed inside the reports. You will also see the current background that we would like to change. Then there is a file that contains the report pages without background that you could use to present the background.

```html
<!DOCTYPE html>
<html lang="en">
<head>
<meta charset="utf-8">
<title>QuorintaFields – Summary of Test Results</title>
<link rel="stylesheet" href="https://fonts.googleapis.com/css2?family=Open+Sans:wght@300;400;700&display=swap">
<style>
  :root {
    --sky: #4cc6f2;
    --sky-pale: #d8f1fc;
    --white: #ffffff;
    --wave-deep: #5a73c4;
    --wave-mid: #7fc3ee;
    --brand: #1a9fe0;
    --title: #1fa8e6;
    --text: #5a5a5a;
    --ok: #2fa95b;
    --alert: #e2292b;
    --figure: #e6e6e6;
  }
  * { margin: 0; padding: 0; box-sizing: border-box; }
  html, body { width: 1200px; height: 1005px; overflow: hidden; background: var(--white); }
  body { font-family: "Open Sans", sans-serif; position: relative; }

  .header-band {
    position: absolute; left: 0; top: 0; width: 1200px; height: 290px;
    background: linear-gradient(180deg, var(--sky) 0%, var(--sky-pale) 60%, var(--white) 100%);
  }
  .header-wave-area {
    position: absolute; left: 0; top: 105px; width: 1200px; height: 175px;
    background:
      radial-gradient(ellipse 300px 60px at 400px 70px, rgba(90,115,196,0.35), transparent 70%),
      radial-gradient(ellipse 340px 70px at 880px 110px, rgba(90,115,196,0.3), transparent 70%),
      radial-gradient(ellipse 260px 50px at 150px 80px, rgba(127,195,238,0.45), transparent 70%);
  }

  .brand {
    position: absolute; left: 820px; top: 146px;
    display: flex; align-items: center; gap: 14px;
  }
  .brand-dot { width: 48px; height: 48px; border-radius: 50%; background: var(--brand); }
  .brand-name { font-size: 30px; font-weight: 400; color: var(--brand); letter-spacing: 0.2px; }

  .report-title {
    position: absolute; left: 89px; top: 369px;
    font-size: 37px; font-weight: 300; color: var(--title); letter-spacing: 0.3px;
  }

  .body-figure {
    position: absolute; left: 466px; top: 568px; width: 270px; height: 437px;
    background: var(--figure); border-radius: 120px 120px 0 0;
  }

  .panel { position: absolute; width: 260px; }
  .panel.left { text-align: right; left: 116px; }
  .panel.right { text-align: left; left: 822px; }
  .panel h2 { font-size: 20px; font-weight: 700; color: var(--title); letter-spacing: 0.3px; height: 26px; margin-bottom: 12px; line-height: 26px; }
  .panel ul { list-style: none; }
  .panel li { font-size: 17.7px; color: var(--text); height: 32px; line-height: 24px; position: relative; }
  .panel.left li::after, .panel.right li::before {
    content: ""; position: absolute; top: 9px; width: 7px; height: 7px; border-radius: 50%;
    background: var(--ok);
  }
  .panel.left li::after { right: -27px; }
  .panel.right li::before { left: -28px; }
  .panel li.alert::after, .panel li.alert::before { background: var(--alert); }

  .blood, .immune { top: 556px; }
  .liver, .heart { top: 790px; }

  .badge {
    position: absolute; width: 66px; height: 66px; border-radius: 50%;
    display: flex; align-items: center; justify-content: center;
  }
  .badge.ok { background: var(--ok); }
  .badge.alert { background: var(--alert); }
</style>
</head>
<body>
  <div class="header-band">
    <div class="header-wave-area" role="img" aria-label="Decorative flowing blue wave lines across the header"></div>
  </div>

  <div class="brand">
    <span class="brand-dot"></span>
    <span class="brand-name">QuorintaFields</span>
  </div>

  <h1 class="report-title">SUMMARY OF TEST RESULTS</h1>

  <div class="body-figure" role="img" aria-label="Grey human silhouette"></div>

  <section class="panel left blood">
    <h2>BLOOD</h2>
    <ul>
      <li>Red blood cells</li>
      <li>Platelets</li>
      <li>Hemoglobin</li>
      <li>Hematocrit</li>
    </ul>
  </section>

  <section class="panel right immune">
    <h2>IMMUNE SYSTEM</h2>
    <ul>
      <li>C-reactive protein</li>
      <li>White blood cells</li>
    </ul>
  </section>

  <section class="panel left liver">
    <h2>LIVER</h2>
    <ul>
      <li class="alert">Alanine transaminase</li>
      <li>Aspartate transaminase</li>
    </ul>
  </section>

  <section class="panel right heart">
    <h2>HEART</h2>
    <ul>
      <li>Cholesterol</li>
      <li>Triglycerides</li>
      <li class="alert">Potassium</li>
    </ul>
  </section>

  <div class="badge ok" style="left:430px; top:622px;">
    <svg width="40" height="40" viewBox="0 0 40 40" fill="var(--white)">
      <path d="M15 6 C15 6 5 18 5 24 a10 10 0 0 0 20 0 C25 18 15 6 15 6z"/>
      <path d="M30 16 C30 16 24 24 24 28 a6 6 0 0 0 12 0 C36 24 30 16 30 16z"/>
    </svg>
  </div>

  <div class="badge ok" style="left:694px; top:622px;">
    <svg width="44" height="44" viewBox="0 0 44 44" fill="var(--white)">
      <circle cx="22" cy="22" r="10"/>
      <circle cx="8" cy="10" r="3"/>
      <circle cx="36" cy="10" r="3"/>
      <circle cx="8" cy="34" r="3"/>
      <circle cx="36" cy="34" r="3"/>
    </svg>
  </div>

  <div class="badge alert" style="left:430px; top:854px;">
    <svg width="42" height="30" viewBox="0 0 42 30" fill="var(--white)">
      <path d="M2 8 C2 3 8 1 20 2 C32 3 40 2 40 7 C40 13 30 16 22 22 C16 27 8 28 5 22 C2 16 2 12 2 8z"/>
    </svg>
  </div>

  <div class="badge alert" style="left:694px; top:854px;">
    <svg width="36" height="34" viewBox="0 0 36 34" fill="var(--white)">
      <path d="M18 32 C8 24 2 18 2 11 a8 8 0 0 1 16 -3 a8 8 0 0 1 16 3 C34 18 28 24 18 32z"/>
    </svg>
  </div>
</body>
</html>
```